Product Packaging for an Aquarium Company
Brivan Aquatics
Product Packaging for an Aquarium Company - Animals
Creative Brief
Our company, Brivan Aquatics is looking for a design for custom packaging to support our main line of aquariums. We are different from other companies as we have a product that is stylish, refined, and elegant. They feature smooth lines and sharp color contrasts.
Animals
We are in the business of wholesale and distribution with the end point being retailers in the aquatic or pet hobby.
The custom packaging design will have to have our logo and company name, Brivan Aquatics visible on the front of the packaging. I want the packaging to reflect the style of our aquariums. I will upload some photos for inspiration. I want to have a white bottle or packaging, or a subtle grey/silver with a sharp contrast of another color. I would be interested to see the addition of a wave or large bubble that would contain the picture of the contents of the packaging.

```html
<!DOCTYPE html>
<html lang="en">
<head>
<meta charset="utf-8">
<title>Brivan Aquatics – Bottle Label</title>
<link rel="stylesheet" href="https://fonts.googleapis.com/css2?family=Cormorant+Garamond:wght@500&family=Arimo&display=swap">
<style>
  :root {
    --stage: #000000;
    --paper: #ffffff;
    --ink: #222222;
    --wave-blue: #1e4fa0;
    --swoosh: #3a3a3a;
    --photo-green: #3f8a2c;
    --photo-light: #8fc95a;
    --photo-dark: #1f4a17;
    --cap: #bfc2c4;
    --caption: #ffffff;
  }
  html, body { margin: 0; padding: 0; overflow: hidden; background: var(--stage); }
  .canvas { position: relative; width: 1200px; height: 742px; background: var(--stage); overflow: hidden; }
  .label-flat { position: absolute; left: 370px; top: 155px; width: 220px; height: 475px; }
  .bottle { position: absolute; left: 690px; top: 80px; width: 190px; height: 550px; }
  .brand-name {
    font-family: "Cormorant Garamond", serif;
    font-weight: 500; font-size: 22px; fill: var(--ink); letter-spacing: 0.5px;
  }
  .spec-caption {
    position: absolute; left: 370px; top: 655px; width: 220px; margin: 0;
    text-align: center; color: var(--caption);
    font-family: "Arimo", sans-serif; font-size: 13px; line-height: 15px;
  }
</style>
</head>
<body>
<div class="canvas">
  <svg class="label-flat" viewBox="0 0 220 475" xmlns="http://www.w3.org/2000/svg">
    <defs>
      <linearGradient id="photoTone" x1="0" y1="0" x2="1" y2="1">
        <stop offset="0" stop-color="var(--photo-light)"/>
        <stop offset="0.5" stop-color="var(--photo-green)"/>
        <stop offset="1" stop-color="var(--photo-dark)"/>
      </linearGradient>
    </defs>
    <rect class="label-paper" width="220" height="475" fill="var(--paper)"/>
    <circle class="brand-dot" cx="108" cy="50" r="22" fill="none" stroke="var(--ink)" stroke-width="2"/>
    <text class="brand-name" x="110" y="102" text-anchor="middle">Brivan Aquatics</text>
    <path class="product-photo" role="img" aria-label="Photo of a red and white shrimp on green aquatic plants"
          d="M0 270 C70 250 150 215 220 222 L220 475 L0 475 Z" fill="url(#photoTone)"/>
    <path class="wave-band" d="M0 262 C70 240 150 205 220 212" fill="none" stroke="var(--wave-blue)" stroke-width="10"/>
    <path class="bottom-sweep" d="M0 475 L0 455 C60 420 140 405 220 410 L220 475 Z" fill="var(--paper)"/>
    <path class="bottom-swoosh" d="M0 462 C60 428 140 413 220 418" fill="none" stroke="var(--swoosh)" stroke-width="8"/>
  </svg>

  <svg class="bottle" viewBox="0 0 190 550" xmlns="http://www.w3.org/2000/svg">
    <defs>
      <linearGradient id="bottleShade" x1="0" y1="0" x2="1" y2="0">
        <stop offset="0" stop-color="#d9d9d9"/>
        <stop offset="0.15" stop-color="#ffffff"/>
        <stop offset="0.85" stop-color="#ffffff"/>
        <stop offset="1" stop-color="#d0d0d0"/>
      </linearGradient>
      <linearGradient id="photoToneB" x1="0" y1="0" x2="1" y2="1">
        <stop offset="0" stop-color="var(--photo-light)"/>
        <stop offset="0.5" stop-color="var(--photo-green)"/>
        <stop offset="1" stop-color="var(--photo-dark)"/>
      </linearGradient>
      <clipPath id="bottleBody"><rect x="0" y="40" width="190" height="510" rx="22"/></clipPath>
    </defs>
    <rect class="bottle-cap" x="55" y="0" width="80" height="48" rx="4" fill="var(--cap)"/>
    <rect class="bottle-body" x="0" y="40" width="190" height="510" rx="22" fill="url(#bottleShade)"/>
    <g clip-path="url(#bottleBody)">
      <path class="product-photo" role="img" aria-label="Photo of a red and white shrimp on green aquatic plants"
            d="M0 392 C60 372 130 345 190 350 L190 550 L0 550 Z" fill="url(#photoToneB)"/>
      <path class="wave-band" d="M0 384 C60 362 130 335 190 340" fill="none" stroke="var(--wave-blue)" stroke-width="10"/>
      <path class="bottom-sweep" d="M0 550 L0 520 C55 490 125 478 190 482 L190 550 Z" fill="url(#bottleShade)"/>
      <path class="bottom-swoosh" d="M0 528 C55 498 125 486 190 490" fill="none" stroke="var(--swoosh)" stroke-width="8"/>
    </g>
    <circle class="brand-dot" cx="95" cy="172" r="20" fill="none" stroke="var(--ink)" stroke-width="2"/>
    <text class="brand-name" x="95" y="218" text-anchor="middle">Brivan Aquatics</text>
  </svg>

  <p class="spec-caption">Label bottle 10 X 9 CM<br>500 ML</p>
</div>
</body>
</html>
```